Modern Podcast Marketing Cards - BRAVOKESTRAL

Update: Do "not" include my address, there's no need for this. Please remember this project needs to promote my brand along with the my new Podcast shows tagline. So this is not a traditional business card, it has to look cool enough so people want to hold onto it and not just toss it aside. So obviously "not" an old school boring business card with a ton of business contact info/text. Needs to catch attention and drive my recipients to want to visit the website " bravokestral.net " and/or to download and listen on the apps Tunevale, Weavly, Mondro Spin. Plus would like to drive them to Follow on my social media channels @BRAVOKESTRAL; all while making sure the the design doesn't look cluttered while not being boring.
I've re-designed the logo specifically for the new show though vs what you see when you first visit my website. So the shows logo is also attached which is found on Tunevale, Weavly app, etc. That design is to promote the three domains this brand focused on "Fueling" the followers and listeners with, regarding "Health", "Business", and "Lifestyle". If logos end up on both sides of the card, one should have the version with the three words included of Health, Business, and Lifestyle. The other side should use the blank version of the logo attached which does not have those three words under the BRAVOKESTRAL logo. So I gave you two versions to work with.
**Try and work in my three domains mentioned above and/or the actual tagline for the show/my brand which is "SPARK Your Health, Business, and Lifestyle". You can break it up a little if it will stand out stronger. Remember this is more of a marketing/advertising card vs a boring traditional business card.
Just to note, my profession behind the Podcast Host is my consulting as a Sales, Marketing, and Business Development consultant, But the final design should really show off my Tagline and those three domains to "SPARK Your Health, Business, and Lifestyle!" (without being cluttered)
- again I like it when the flames get ghosted or used as a transparent backdrop. Or you can somehow take a podcast microphone and overlay my logo's flames to wrap around the microphone or have the microphone stand out with "fire fueling it".
Why the three domains focus?
1. Health: because I'm a health nut, adrenaline junkie sports participant, GritLoop coach, and I have a part time nutritional business.
2. Business: because I'm a business consultant specializing in online branding and social media marketing, with 20 years of business experience.
3. Lifestyle: because I do a lot of coaching on life balance, motivational speaking, love to travel, and am always promoting people to balance their lifestyle between business, personal, and fun.

Target Market(s)

Podcasting, Online Branding & Marketing

Industry/Entity Type

Marketing

Contact Information for Business Card

More of a marketing card than a traditional business card, Double-sided, rich bold colors used from my logo's colors. Will consider the clear plastic style too.

Font styles to use
Serif
Sans Serif

Requirements
Must have
• - Drive people to want to visit the website and download/listen to my podcast via the three apps.
• - So use those apps logos somehow from Tunevale Podcast app, Weavly Radio app, and the Mondro Spin app logos.
• - For contact info: My Name, Titles are Chief Intrepid Officer, also include Podcaster for the 2nd title. Contact info should be 1st my email, 2nd my website address without the www; and third my phone.
• Note: reduce clutter and make sure it's not too busy. That's why I'm considering a 2 sided design.
Nice to have
• - Colors should coincide with my logo and primary colors from the logos.
• - Not too much white, at least side should be a gray or blue backdrop
• - I love the style where you take the flames from my logo and ghost or make them transparent on the backdrop for the background on the card.
• - A podcast microphone logo included somehow or set it one fire with my fire from my logo would be cool.
Should not have
• - Do not list my address
• - No single sided cards
• - No crazy stripes or swoosh marks, emphasis is the FIRE so motivate people, and inspire, "to fire them up" with your design.

```html
<!DOCTYPE html>
<html lang="en">
<head>
<meta charset="utf-8">
<title>BRAVOKESTRAL – Podcast Marketing Cards</title>
<link href="https://fonts.googleapis.com/css2?family=Bebas+Neue&family=Oswald:wght@500;600&family=Open+Sans:wght@400;600&display=swap" rel="stylesheet">
<style>
  :root {
    --navy: #1c2658;
    --navy-deep: #141c48;
    --navy-soft: #56638f;
    --navy-mist: #7b87ad;
    --ink: #2b2b2b;
    --grey: #6b6b6b;
    --ghost: #f1f1f3;
    --paper: #ffffff;
    --backdrop: #e6e4e1;
    --badge-light: #d8d8d8;
    --badge-mid: #b0b0b0;
    --badge-dark: #8a8a8a;
  }
  * { margin: 0; padding: 0; box-sizing: border-box; }
  html, body { width: 1200px; height: 886px; overflow: hidden; }
  body {
    background: var(--backdrop);
    display: flex;
    flex-direction: column;
    align-items: center;
    justify-content: center;
    gap: 30px;
  }
  .card {
    position: relative;
    width: 700px;
    height: 400px;
    border-radius: 4px;
    overflow: hidden;
    box-shadow: 0 6px 18px rgba(0,0,0,.18);
  }

  /* Back side */
  .card--back {
    background: linear-gradient(135deg, var(--navy) 0%, var(--navy-deep) 100%);
    color: var(--navy-mist);
  }
  .back-emblem {
    position: absolute;
    left: 220px; top: 36px;
    width: 260px; height: 200px;
    overflow: hidden;
  }
  .back-emblem__disc {
    width: 260px; height: 260px;
    border-radius: 50%;
    background: var(--navy-soft);
  }
  .back-emblem__name {
    position: absolute;
    left: 0; right: 0; top: 92px;
    text-align: center;
    font-family: "Bebas Neue", sans-serif;
    font-size: 40px;
    letter-spacing: 1px;
    color: var(--navy);
  }
  .back-tagline {
    position: absolute;
    left: 0; right: 0; top: 244px;
    text-align: center;
    font-family: "Oswald", sans-serif;
    font-weight: 500;
    font-size: 15px;
    letter-spacing: 1.5px;
    text-transform: uppercase;
  }
  .back-rule {
    position: absolute;
    left: 200px; width: 300px; height: 1px;
    background: var(--navy-soft);
  }
  .back-rule--upper { top: 274px; }
  .back-rule--lower { top: 306px; }
  .back-handle {
    position: absolute;
    left: 0; right: 0; top: 280px;
    text-align: center;
    font-family: "Oswald", sans-serif;
    font-weight: 500;
    font-size: 14px;
    letter-spacing: 1px;
  }
  .social-row {
    position: absolute;
    left: 0; right: 0; top: 318px;
    display: flex;
    justify-content: center;
    gap: 9px;
  }
  .social-row span {
    width: 22px; height: 22px;
    border-radius: 50%;
    background: var(--navy-soft);
  }

  /* Front side */
  .card--front { background: var(--paper); }
  .front-ghost {
    position: absolute;
    left: 60px; top: 150px;
    width: 230px; height: 230px;
    border-radius: 50%;
    background: radial-gradient(circle, var(--ghost) 0%, rgba(241,241,243,0) 70%);
  }
  .front-brand {
    position: absolute;
    right: 48px; top: 20px;
    width: 170px;
    text-align: center;
  }
  .front-brand__disc {
    width: 90px; height: 90px;
    margin: 0 auto;
    border-radius: 50%;
    background: var(--navy);
  }
  .front-brand__name {
    font-family: "Bebas Neue", sans-serif;
    font-size: 34px;
    line-height: 1;
    margin-top: 6px;
    color: var(--navy);
  }
  .front-brand__domains {
    font-family: "Oswald", sans-serif;
    font-weight: 500;
    font-size: 10px;
    letter-spacing: 2px;
    color: var(--navy);
  }
  .app-badges {
    position: absolute;
    right: 52px; top: 172px;
    display: flex;
    flex-direction: column;
    gap: 5px;
  }
  .app-badges span {
    width: 78px; height: 17px;
    border-radius: 3px;
    background: var(--badge-dark);
  }
  .app-badges span:nth-child(1) { background: var(--badge-light); }
  .app-badges span:nth-child(2) { background: var(--badge-mid); }
  .front-divider {
    position: absolute;
    left: 40px; right: 40px; top: 252px;
    height: 1px;
    background: var(--navy);
  }
  .person {
    position: absolute;
    left: 40px; top: 214px;
  }
  .person__name {
    font-family: "Bebas Neue", sans-serif;
    font-size: 34px;
    font-weight: 400;
    line-height: 1;
    letter-spacing: .5px;
    color: var(--navy);
  }
  .person__title {
    margin-top: 10px;
    font-family: "Oswald", sans-serif;
    font-weight: 600;
    font-size: 12px;
    line-height: 16px;
    letter-spacing: .5px;
    color: var(--ink);
  }
  .person__rule {
    position: absolute;
    left: 40px; top: 290px;
    width: 180px; height: 1px;
    background: #b8b8b8;
  }
  .contact-list {
    position: absolute;
    left: 40px; top: 298px;
    list-style: none;
    font-family: "Open Sans", sans-serif;
    font-size: 13px;
    color: var(--grey);
  }
  .contact-list li {
    display: flex;
    align-items: center;
    gap: 10px;
    height: 20px;
  }
  .contact-list svg { width: 13px; height: 13px; fill: var(--navy); }
  .front-band-line {
    position: absolute;
    left: 0; right: 0; top: 372px;
    height: 1px;
    background: var(--navy);
  }
  .front-band {
    position: absolute;
    left: 0; right: 0; top: 378px; bottom: 0;
    background: var(--navy);
  }
</style>
</head>
<body>

<section class="card card--back" aria-label="Card back">
  <div class="back-emblem">
    <div class="back-emblem__disc"></div>
    <div class="back-emblem__name">BRAVOKESTRAL</div>
  </div>
  <p class="back-tagline">Spark your health, business &amp; lifestyle</p>
  <div class="back-rule back-rule--upper"></div>
  <p class="back-handle">@BRAVOKESTRAL</p>
  <div class="back-rule back-rule--lower"></div>
  <div class="social-row" aria-label="Social channels">
    <span></span><span></span><span></span><span></span><span></span><span></span><span></span><span></span>
  </div>
</section>

<section class="card card--front" aria-label="Card front">
  <div class="front-ghost" role="img" aria-label="Faint ghosted flame backdrop"></div>

  <div class="front-brand">
    <div class="front-brand__disc"></div>
    <div class="front-brand__name">BRAVOKESTRAL</div>
    <div class="front-brand__domains">BODY | BUSINESS | LIFE</div>
  </div>

  <div class="app-badges" aria-label="Listen on Tunevale, Weavly and Mondro Spin">
    <span></span><span></span><span></span>
  </div>

  <div class="person">
    <h1 class="person__name">DORIAN WHITLOCK</h1>
    <p class="person__title">CHIEF INTREPID OFFICER | PODCASTER</p>
  </div>
  <div class="front-divider"></div>
  <div class="person__rule"></div>

  <ul class="contact-list">
    <li>
      <svg viewBox="0 0 16 16" aria-hidden="true"><path d="M1 3h14v10H1zM2.2 4.2v.4L8 8.6l5.8-4v-.4z"/></svg>
      dorian@bravokestral.net
    </li>
    <li>
      <svg viewBox="0 0 16 16" aria-hidden="true"><circle cx="8" cy="8" r="7"/><path d="M1 8h14M8 1c-3 3.5-3 10.5 0 14M8 1c3 3.5 3 10.5 0 14" stroke="#fff" stroke-width="1" fill="none"/></svg>
      bravokestral.net
    </li>
    <li>
      <svg viewBox="0 0 16 16" aria-hidden="true"><path d="M3.6 1.2l2.2 2.6-1.3 1.8c.9 2 2.5 3.6 4.5 4.5l1.8-1.3 2.6 2.2-1 2.6C7 13.4 2.6 9 2.4 2.2z"/></svg>
      555-014-2278
    </li>
  </ul>

  <div class="front-band-line"></div>
  <div class="front-band"></div>
</section>

</body>
</html>
```